SaaS Early tech startup business card design

Unique design for experience ecommerce platform company. the business cards will be used by executive members. conformance with color code is required.

```html
<!DOCTYPE html>
<html lang="en">
<head>
<meta charset="utf-8">
<title>Velora Business Card</title>
<link rel="stylesheet" href="https://fonts.googleapis.com/css2?family=Nunito:wght@800&family=Open+Sans:wght@400;700&display=swap">
<style>
  :root {
    --backdrop: #1e1e1e;
    --brand-blue: #17668f;
    --brand-teal: #20b596;
    --paper: #ffffff;
    --ink-light: #ffffff;
  }
  * { margin: 0; padding: 0; box-sizing: border-box; }
  html, body {
    width: 1200px; height: 988px; overflow: hidden;
    background: var(--backdrop);
  }
  .sheet {
    position: relative; width: 1200px; height: 988px;
    display: flex; flex-direction: column; align-items: center; justify-content: center; gap: 60px;
  }
  .card {
    position: relative; width: 700px; height: 400px;
    border-radius: 26px; overflow: hidden;
    background: var(--brand-blue);
  }
  .card-front { display: flex; align-items: center; justify-content: center; }
  .wordmark {
    font-family: "Nunito", sans-serif; font-weight: 800;
    color: var(--brand-teal); letter-spacing: -2px; line-height: 1;
  }
  .card-front .wordmark { font-size: 150px; }
  .back-art { position: absolute; inset: 0; }
  .card-back .wordmark {
    position: absolute; left: 450px; top: 92px; font-size: 88px;
  }
  .details {
    position: absolute; left: 52px; top: 118px;
    font-family: "Open Sans", sans-serif; color: var(--ink-light);
  }
  .person-name { font-size: 30px; font-weight: 700; line-height: 1.1; }
  .person-role { font-size: 17px; margin-top: 2px; }
  .address { font-size: 17px; line-height: 1.35; margin-top: 30px; padding-left: 30px; white-space: nowrap; }
  .contact-list { list-style: none; margin-top: 26px; padding-left: 30px; font-size: 17px; line-height: 1.45; }
  .contact-list li { display: flex; align-items: center; gap: 9px; }
  .contact-list svg { width: 14px; height: 14px; flex: none; }
</style>
</head>
<body>
  <main class="sheet">
    <section class="card card-front" aria-label="Card front">
      <span class="wordmark">velora</span>
    </section>

    <section class="card card-back" aria-label="Card back">
      <svg class="back-art" viewBox="0 0 700 400" aria-hidden="true">
        <circle cx="570" cy="135" r="245" fill="none" stroke="var(--brand-teal)" stroke-width="5"/>
        <circle cx="578" cy="128" r="234" fill="var(--paper)"/>
      </svg>
      <span class="wordmark">velora</span>

      <div class="details">
        <h1 class="person-name">Elin Marsh</h1>
        <p class="person-role">Managing Director</p>
        <p class="address">Your location street here,<br>Country name, Country - 91542</p>
        <ul class="contact-list">
          <li>
            <svg viewBox="0 0 16 16"><path fill="#fff" d="M3.5 1 6 3.6 4.8 5.6a9 9 0 0 0 5.6 5.6l2-1.2L15 12.5 13.4 15C7 15 1 9 1 2.6Z"/></svg>
            +012 345 6789
          </li>
          <li>
            <svg viewBox="0 0 16 16"><rect x="1" y="3" width="14" height="10" rx="1" fill="#fff"/><path d="M1.5 3.5 8 9l6.5-5.5" fill="none" stroke="#17668f" stroke-width="1.4"/></svg>
            info@youremail.com
          </li>
          <li>
            <svg viewBox="0 0 16 16"><circle cx="8" cy="8" r="6.5" fill="none" stroke="#fff" stroke-width="1.6"/><path d="M1.5 8h13M8 1.5c-3 3.5-3 9.5 0 13M8 1.5c3 3.5 3 9.5 0 13" fill="none" stroke="#fff" stroke-width="1.2"/></svg>
            www.yourwebsite.com
          </li>
        </ul>
      </div>
    </section>
  </main>
</body>
</html>
```